Awesome Digital Ad Design – Pellucid Adreach

I am going to be setting up a Pellucid Adreach ad campaign I need creatives for.

Several sizes are needed in the end, however, please submit your design concept in the following 2 sizes to start:
Medium rectangle: 300X250
Leaderboard: 728X90

Original artwork/design files and images used expected upon payment and as part of the final delivery.

Ads should match our company brand and the information on this webpage: http://www.harborlyneworks.com/real-estate-marketing/
SEE MORE INSTRUCTIONS IN ATTACHED WORD DOC
Updates

Target Market(s)

Business-To-Business Audience –Real Estate Company Executives (Presidents/VPs/Owners/CEOs/Sales Managers).

Industry/Entity Type

Real Estate

Font styles to use
Sans Serif

Requirements
Must have
• Copy should be minimal words, billboard like. Please use real photos/images that would appeal to real estate high-level decision-maker executives.
Should not have
• No cartoons or graphics

```html
<!DOCTYPE html>
<html lang="en">
<head>
<meta charset="utf-8">
<title>Harborlyne Works – Client Follow-Up Ads</title>
<link href="https://fonts.googleapis.com/css2?family=PT+Sans:wght@400;700&display=swap" rel="stylesheet">
<style>
  :root {
    --canvas: #e6e7e8;
    --band-grey: #6d6d6f;
    --gold: #c9b98e;
    --maroon: #6b2634;
    --ink: #222222;
    --white: #ffffff;
    --orange: #f26a1b;
    --logo-ink: #3a3a3c;
    --photo-light: #eef1f3;
    --photo-siding: #d3dbe2;
    --photo-blue: #aebccb;
    --photo-green: #b9c9a6;
    --photo-suit: #6a5560;
    --photo-suit-deep: #58444c;
  }
  * { box-sizing: border-box; margin: 0; padding: 0; }
  html, body { width: 1200px; height: 1200px; overflow: hidden; }
  body {
    background: var(--canvas);
    font-family: "PT Sans", Arial, sans-serif;
    position: relative;
  }

  /* shared pieces */
  .brand-badge {
    position: absolute;
    border-radius: 50%;
    background: var(--white);
    border: 3px solid #dcdcdc;
    display: flex;
    align-items: center;
    justify-content: center;
    text-align: center;
    color: var(--logo-ink);
    font-weight: 400;
    line-height: 1.05;
  }
  .cta {
    position: absolute;
    background: var(--orange);
    color: var(--white);
    border-radius: 6px;
    font-weight: 700;
    display: flex;
    align-items: center;
    justify-content: center;
    letter-spacing: 0.2px;
  }
  .tagline { position: absolute; color: var(--white); text-align: center; }
  .headline { position: absolute; text-align: center; color: var(--ink); font-weight: 400; }
  .headline .lead { display: block; color: var(--maroon); font-weight: 700; letter-spacing: -0.5px; }
  .headline .sub { display: block; letter-spacing: -0.4px; }

  /* medium rectangle 300x250 */
  .ad-rectangle {
    position: absolute;
    left: 353px; top: 254px;
    width: 494px; height: 408px;
    overflow: hidden;
    background: var(--white);
  }
  .ad-rectangle .photo {
    position: absolute; left: 0; top: 79px;
    width: 100%; height: 325px;
    background:
      linear-gradient(0deg, rgba(185,201,166,0.9) 0%, rgba(185,201,166,0) 30%),
      linear-gradient(90deg, var(--photo-light) 0%, var(--photo-siding) 30%, var(--photo-blue) 46%, #c6d0d8 52%, var(--photo-suit) 62%, var(--photo-suit-deep) 80%, var(--photo-suit) 100%);
  }
  .ad-rectangle .top-band {
    position: absolute; left: 0; top: 0;
    width: 100%; height: 79px;
    background: var(--band-grey);
    border-bottom: 4px solid var(--gold);
  }
  .ad-rectangle .bottom-rule {
    position: absolute; left: 0; bottom: 0; width: 100%; height: 4px; background: var(--gold);
  }
  .ad-rectangle .brand-badge {
    left: 40px; top: 13px; width: 126px; height: 126px; font-size: 17px;
  }
  .ad-rectangle .tagline {
    left: 303px; top: 12px; width: 160px; font-size: 20px; line-height: 27px;
  }
  .ad-rectangle .headline { left: 20px; top: 186px; width: 200px; }
  .ad-rectangle .headline .lead { font-size: 50px; line-height: 50px; }
  .ad-rectangle .headline .sub { font-size: 29px; line-height: 36px; }
  .ad-rectangle .cta {
    left: 21px; top: 339px; width: 197px; height: 47px; font-size: 20px;
  }

  /* leaderboard 728x90 */
  .ad-leaderboard {
    position: absolute;
    left: 97px; top: 761px;
    width: 1002px; height: 123px;
    overflow: hidden;
    background: var(--white);
  }
  .ad-leaderboard .photo {
    position: absolute; left: 174px; top: 0; width: 591px; height: 100%;
    background: linear-gradient(90deg, var(--white) 0%, var(--white) 24%, #e3e8ec 36%, var(--photo-siding) 48%, var(--photo-blue) 62%, #c6d0d8 68%, var(--photo-suit) 80%, var(--photo-suit-deep) 92%, var(--photo-suit) 100%);
  }
  .ad-leaderboard .side-panel {
    position: absolute; top: 0; height: 100%; background: var(--band-grey);
  }
  .ad-leaderboard .side-panel.left { left: 0; width: 174px; border-right: 5px solid var(--gold); }
  .ad-leaderboard .side-panel.right { left: 761px; right: 0; border-left: 4px solid var(--gold); }
  .ad-leaderboard .brand-badge {
    left: 32px; top: 8px; width: 108px; height: 108px; font-size: 15px;
  }
  .ad-leaderboard .headline { left: 219px; top: 12px; width: 200px; }
  .ad-leaderboard .headline .lead { font-size: 40px; line-height: 42px; }
  .ad-leaderboard .headline .sub { font-size: 22px; line-height: 31px; }
  .ad-leaderboard .tagline {
    left: 781px; top: 11px; width: 200px; font-size: 17px; line-height: 24px;
  }
  .ad-leaderboard .cta {
    left: 805px; top: 69px; width: 165px; height: 41px; font-size: 18px;
  }
</style>
</head>
<body>

  <section class="ad-rectangle" aria-label="Medium rectangle ad">
    <div class="photo" role="img" aria-label="Photo of a smiling real estate agent holding a sold sign in front of a house"></div>
    <div class="top-band"></div>
    <div class="bottom-rule"></div>
    <div class="brand-badge">Harborlyne<br>Works</div>
    <p class="tagline">Virtually No Cost<br>To Your Company!</p>
    <h2 class="headline">
      <span class="lead">CLIENT</span>
      <span class="sub">FOLLOW-UP</span>
      <span class="sub">MADE SIMPLE</span>
    </h2>
    <div class="cta">LEARN MORE</div>
  </section>

  <section class="ad-leaderboard" aria-label="Leaderboard ad">
    <div class="photo" role="img" aria-label="Photo of a smiling real estate agent in front of a house"></div>
    <div class="side-panel left"></div>
    <div class="side-panel right"></div>
    <div class="brand-badge">Harborlyne<br>Works</div>
    <h2 class="headline">
      <span class="lead">CLIENT</span>
      <span class="sub">FOLLOW-UP</span>
      <span class="sub">MADE SIMPLE</span>
    </h2>
    <p class="tagline">Virtually No Cost<br>To Your Company!</p>
    <div class="cta">LEARN MORE</div>
  </section>

</body>
</html>
```